Need a Facebook image for childcare advertisement

We are after a design for Facebook advertisement for childcare and kindergarten centre enrolments for 2023.

I have attached a previous flyer that we have in pdf format. The new logo is also attached with this brief.

All other information is still current as per the attached flyer.

You can use same colours as per attached flyer. I will also attached some stock images that you can select to use for the design.

our website for your reference:

https://tolvenbrook.com.au

```html
<!DOCTYPE html>
<html lang="en">
<head>
<meta charset="utf-8">
<title>Tolvenbrook – Enrolments 2023</title>
<link href="https://fonts.googleapis.com/css2?family=Baloo+2:wght@600;700;800&family=Open+Sans:wght@400&display=swap" rel="stylesheet">
<style>
  :root {
    --navy: #003f87;
    --sky: #4ba9e1;
    --white: #ffffff;
    --cloud: #e3e8ec;
    --cloud-edge: #d5dbe0;
    --sun: #f3c12c;
    --ink: #2b2b2b;
  }
  html, body { margin: 0; padding: 0; overflow: hidden; background: #ececec; }
  .ad {
    position: relative;
    width: 1200px; height: 1200px;
    background: var(--navy);
    overflow: hidden;
    font-family: "Baloo 2", sans-serif;
  }
  .ad__shapes { position: absolute; inset: 0; }
  .brand {
    position: absolute; left: 70px; top: 90px; width: 340px;
    text-align: center;
  }
  .brand__name {
    display: inline-flex; align-items: center; gap: 14px;
    font-weight: 800; font-size: 58px; line-height: 1; color: var(--navy);
  }
  .brand__dot { width: 26px; height: 26px; border-radius: 50%; background: var(--sun); }
  .brand__tagline {
    margin-top: 18px;
    font-family: "Open Sans", sans-serif; font-size: 18px; letter-spacing: 0.3px;
    color: var(--ink);
  }
  .headline { position: absolute; left: 61px; top: 500px; margin: 0; font-weight: 800; }
  .headline__main { display: block; color: var(--sky); font-size: 80px; line-height: 76px; }
  .headline__sub { display: block; color: var(--white); font-size: 58px; line-height: 62px; margin-top: 4px; }
  .headline__year { display: block; color: var(--white); font-size: 122px; line-height: 112px; }
  .cta {
    position: absolute; left: 61px; top: 972px; margin: 0;
    color: var(--sky); font-weight: 700; font-size: 43px; line-height: 1;
  }
  .contact {
    position: absolute; left: 61px; top: 1040px;
    list-style: none; margin: 0; padding: 0;
    color: var(--white); font-weight: 700; font-size: 29px; line-height: 34px;
  }
</style>
</head>
<body>
<main class="ad">
  <svg class="ad__shapes" width="1200" height="1200" viewBox="0 0 1200 1200">
    <defs>
      <clipPath id="frame-clip"><circle cx="930" cy="370" r="430"/></clipPath>
      <clipPath id="photo-clip"><circle cx="972" cy="350" r="412"/></clipPath>
      <linearGradient id="photo-tones" x1="0" y1="0" x2="1" y2="1">
        <stop offset="0" stop-color="#e9d7b8"/>
        <stop offset="0.45" stop-color="#d8738f"/>
        <stop offset="0.75" stop-color="#b4463a"/>
        <stop offset="1" stop-color="#7a5a48"/>
      </linearGradient>
      <path id="cloud-shape" d="M10,60 C0,60 0,45 12,42 C12,30 28,25 38,32 C45,10 80,5 92,25 C105,18 125,28 122,42 C140,40 148,60 135,60 Z"/>
    </defs>

    <g class="photo-frame" clip-path="url(#frame-clip)">
      <circle class="photo-frame__ring" cx="930" cy="370" r="430" fill="var(--sun)"/>
      <rect x="500" y="-60" width="900" height="900" fill="url(#photo-tones)" clip-path="url(#photo-clip)" role="img" aria-label="Photo of young children painting together at a classroom table"/>
    </g>

    <path class="brand-cloud" d="M0,0 H662 C645,120 585,215 505,252 C485,300 420,305 382,282 C350,322 268,322 230,284 C188,304 120,294 108,254 C78,272 30,264 0,240 Z" fill="var(--white)" stroke="var(--cloud-edge)" stroke-width="4"/>

    <use href="#cloud-shape" transform="translate(510,67) scale(0.53,0.78)" fill="var(--cloud)"/>
    <use href="#cloud-shape" transform="translate(513,506) scale(1.04,1.05)" fill="var(--cloud)"/>
    <use href="#cloud-shape" transform="translate(883,844) scale(1.02,1.05)" fill="var(--cloud)"/>

    <path class="ground-cloud" d="M589,1200 C600,1160 660,1140 700,1160 C720,1110 790,1100 820,1150 C850,1130 880,1135 900,1160 C920,1100 980,1080 1010,1110 C1030,1020 1120,990 1160,1040 C1180,1045 1195,1060 1200,1070 V1200 Z" fill="var(--white)" stroke="var(--cloud-edge)" stroke-width="4"/>
  </svg>

  <div class="brand">
    <div class="brand__name"><span class="brand__dot"></span>Tolvenbrook</div>
    <div class="brand__tagline">EARLY CHILDHOOD LEARNING CENTRE</div>
  </div>

  <h1 class="headline">
    <span class="headline__main">Childcare &amp;</span>
    <span class="headline__main">kindergarten</span>
    <span class="headline__main">Centre</span>
    <span class="headline__sub">enrolments for</span>
    <span class="headline__year">2023</span>
  </h1>

  <p class="cta">Contact us to secure your child's spot</p>

  <ul class="contact">
    <li>(03) 9012 4476</li>
    <li>admin@tolvenbrook.com.au</li>
    <li>https://www.tolvenbrook.com.au/</li>
  </ul>
</main>
</body>
</html>
```